BrivoPeak Business Card Design Project

We are looking for a modern, clean business card design for our new company. We are a consulting firm focused on the financial services market providing management and IT consulting to banks, insurance companies, etc. Please include our company logo and company contact information from the attached file in the design. Two versions of the logo are attached, either version is acceptable. Logos are available in other file formats if needed. We would like to include the contact information for both our UK and US offices as well as the following information for each individual card holder: Name, position/title, address, phone number and e-mail address.
Updates
Project Deadline Extended
Reason: A last minute trip over seas has prevented us from finalizing the decision. A decision will be made this week. We apologize for the inconvenience.
Industry/Entity Type
Business
Contact Information for Business Card
Company logo.
Company locations and phone numbers for both the US and UK offices.
Company URL.
Cardholder Name
Cardholder Position/title
Cardholder Address
Cardholder Phone Number
Cardholder e-mail Address
Look and feel
Each slider illustrates characteristics of the customer's brand and the style your logo design should communicate.

```html
<!DOCTYPE html>
<html lang="en">
<head>
<meta charset="utf-8">
<title>BrivoPeak Partners – Business Card</title>
<link href="https://fonts.googleapis.com/css2?family=Open+Sans:wght@400;600;700&display=swap" rel="stylesheet">
<style>
  :root {
    --backdrop: #98999b;
    --card: #ffffff;
    --navy: #263a5c;
    --slate-blue: #475c7c;
    --band-grey: #656565;
    --ink-grey: #5f5f5f;
    --ink-dark: #222222;
  }
  html, body {
    margin: 0;
    padding: 0;
    overflow: hidden;
    background: var(--backdrop);
  }
  .stage {
    display: block;
    width: 1200px;
    height: 1000px;
  }
  .card-surface { fill: var(--card); }
  .stripe-navy { fill: var(--navy); }
  .stripe-slate { fill: var(--slate-blue); }
  .band-grey { fill: var(--band-grey); }
  .brand-name {
    font-family: "Open Sans", sans-serif;
    font-weight: 700;
    fill: var(--navy);
  }
  .brand-square { fill: var(--navy); }
  .holder-name {
    font-family: "Open Sans", sans-serif;
    font-size: 22px;
    fill: var(--ink-grey);
  }
  .holder-position {
    font-family: "Open Sans", sans-serif;
    font-size: 13px;
    fill: var(--ink-grey);
  }
  .web-address {
    font-family: "Open Sans", sans-serif;
    font-size: 16px;
    fill: #ffffff;
  }
  .contact-line {
    font-family: "Open Sans", sans-serif;
    font-size: 15px;
    fill: var(--ink-dark);
  }
  .icon-tile { fill: var(--navy); }
  .icon-glyph { fill: #ffffff; }
</style>
</head>
<body>
<svg class="stage" width="1200" height="1000" viewBox="0 0 1200 1000" xmlns="http://www.w3.org/2000/svg">

  <!-- Front of card -->
  <g class="card-front">
    <polygon class="card-surface" points="316,138 700,138 790,366 745,464 316,464"/>
    <polygon class="band-grey" points="316,366 762,366 711,464 316,464"/>
    <polygon class="stripe-navy" points="686,138 718,138 812,366 762,464 728,464 780,366"/>
    <polygon class="stripe-slate" points="718,138 792,138 886,366 834,464 762,464 812,366"/>

    <g class="brand-lockup">
      <rect class="brand-square" x="348" y="190" width="22" height="22"/>
      <text class="brand-name" x="380" y="209" font-size="24">BrivoPeak Partners</text>
    </g>

    <text class="holder-name" x="343" y="318">Your Name</text>
    <text class="holder-position" x="343" y="340">Your Position</text>
    <text class="web-address" x="346" y="420">www.brivopeakpartners.com</text>
  </g>

  <!-- Back of card -->
  <g class="card-back">
    <polygon class="card-surface" points="410,556 886,556 886,883 368,883 316,783"/>
    <polygon class="stripe-slate" points="410,556 488,556 394,783 446,883 368,883 316,783"/>
    <polygon class="stripe-navy" points="518,556 550,556 458,783 508,883 476,883 424,783"/>
    <rect class="band-grey" x="600" y="872" width="254" height="11"/>

    <g class="brand-lockup">
      <rect class="brand-square" x="767" y="586" width="22" height="22"/>
      <text class="brand-name" x="778" y="642" font-size="22" text-anchor="middle">BrivoPeak Partners</text>
    </g>

    <g class="contact-block" text-anchor="end">
      <text class="contact-line" x="794" y="714">418 N Harlow Ave, Suite 204-117</text>
      <text class="contact-line" x="794" y="736">Millbrook UT 84120, United States</text>
      <text class="contact-line" x="794" y="764">14-16 Calder Street, London</text>
      <text class="contact-line" x="794" y="786">E2 8QX, Great Britain</text>
      <text class="contact-line" x="794" y="819">(801) 555-0143</text>
      <text class="contact-line" x="794" y="840">+44 7700 900318</text>
    </g>

    <g class="icon-pin">
      <rect class="icon-tile" x="811" y="695" width="44" height="44"/>
      <path class="icon-glyph" d="M833 707c-4 0-7 3-7 7 0 5 7 13 7 13s7-8 7-13c0-4-3-7-7-7zm0 10a2.8 2.8 0 1 1 0-5.6 2.8 2.8 0 0 1 0 5.6z"/>
    </g>
    <g class="icon-pin">
      <rect class="icon-tile" x="811" y="747" width="44" height="44"/>
      <path class="icon-glyph" d="M833 759c-4 0-7 3-7 7 0 5 7 13 7 13s7-8 7-13c0-4-3-7-7-7zm0 10a2.8 2.8 0 1 1 0-5.6 2.8 2.8 0 0 1 0 5.6z"/>
    </g>
    <g class="icon-phone">
      <rect class="icon-tile" x="811" y="800" width="44" height="44"/>
      <path class="icon-glyph" d="M826 812c1-1 2-1 3 0l3 4c1 1 0 2-1 3l-1 1c1 3 4 6 7 7l1-1c1-1 2-2 3-1l4 3c1 1 1 2 0 3l-2 2c-2 2-8 0-13-5s-7-11-5-13z"/>
    </g>
  </g>
</svg>
</body>
</html>
```